PREMIUM AGENCY High End Business Card - A+++ Designers Wanted

** DO NOT ATTEMPT TO CONTACT ME THROUGH SEARCHING ON ZINTREL OR EMAILING ME THROUGH MY WEBSITE **

I need a fresh, contemporary business card designed using the logo attached (BRONSALK)

I have attached the font for BRONSALK

It must have a premium look and feel. The business card size must be STANDARD size.

You can submit either/both VERTICAL or HORIZONTAL designs.

FRONT: It must have the following sample information on

Paul Ardley
Director Operations
Mobile +61 452 118 906
Email paulardley@bronsalk.com
www.bronsalk.com

The REAR of the business card must have the words

CREATE INSPIRE TOMORROW

as part of the design, in the same font (NEXA) attached.

The words do not need to be in capitals, or on the same line, please design this as you see it best working.

ADDITIONAL INFORMATION
======================

The BRONSALK logo must be on the front of the card

I want Ultraviolet printing on the final design, to enhance either the NAME of the person OR the BRONSALK logo OR the words on the back of the card.

Target Market(s)

Agency, Advertising Agency, Creative, Designers

Industry/Entity Type

Media

Contact Information for Business Card

Design Agency, Contemporary, Premium look and feel, High Quality

Font styles to use
Serif
Sans Serif
Other font styles liked:
• ATTACHED TO PROJECT

Requirements
Must have
• BLACK & WHITE as the primary design, and if you feel there can be a highlighted colour, then this can be used.
• The Logo ICON attached is blue, this colour must not be changed.
• I have attached the partner brand BRONSALK MEDIA incase you need to manipulate the original files.
• ** DO NOT ATTEMPT TO CONTACT ME THROUGH SEARCHING ON ZINTREL OR EMAILING ME THROUGH MY WEBSITE **
Nice to have
• Must be Premium. I have attached some sample designs, that I like that would be a good inspiration for where this can be taken.
• My favourite design is is the KESTRAVUE2-BUSINESSCARD-TEMPLATE
Should not have
• No funny or silly standard / off the shelf designs

```html
<!DOCTYPE html>
<html lang="en">
<head>
<meta charset="utf-8">
<title>Bronsalk Media – Business Card</title>
<link rel="stylesheet" href="https://fonts.googleapis.com/css2?family=Montserrat:wght@300;400;600;700&display=swap">
<style>
  :root {
    --backdrop: #eee9e3;
    --card-black: #19191b;
    --card-clear: #e2cdb5;
    --card-clear-deep: #d8b994;
    --ink-white: #ffffff;
  }
  * { margin: 0; padding: 0; box-sizing: border-box; }
  html, body {
    width: 1189px; height: 1200px; overflow: hidden;
    background: var(--backdrop);
    font-family: "Montserrat", sans-serif;
    color: var(--ink-white);
  }
  .canvas { position: relative; width: 1189px; height: 1200px; }
  .card {
    position: absolute; width: 764px; height: 436px;
    background: var(--card-black); overflow: hidden;
    box-shadow: 0 18px 40px rgba(60, 40, 20, 0.18);
  }
  .card--front { left: 315px; top: 130px; }
  .card--back { left: 121px; top: 646px; }

  .clear-panel {
    position: absolute; top: 0; bottom: 0; width: 150px;
    background: linear-gradient(180deg, var(--card-clear), var(--card-clear-deep));
  }
  .card--front .clear-panel { left: 0; }
  .card--back .clear-panel { right: 0; }

  .wordmark {
    position: absolute; display: flex; align-items: center; gap: 16px;
    font-weight: 600; letter-spacing: 0.09em; white-space: nowrap; line-height: 1;
  }
  .wordmark__dot {
    width: 26px; height: 26px; border: 3px solid var(--ink-white); border-radius: 50%;
  }
  .card--front .wordmark { right: 44px; top: 170px; font-size: 40px; }
  .card--back .wordmark { left: 41px; top: 180px; font-size: 47px; letter-spacing: 0.08em; }

  .person { position: absolute; right: 44px; top: 255px; text-align: right; }
  .person__name { font-weight: 700; font-size: 26px; letter-spacing: 0.01em; line-height: 1; }
  .person__role { font-weight: 400; font-size: 20px; margin-top: 4px; }

  .contacts {
    position: absolute; right: 44px; top: 328px; list-style: none;
    font-size: 19px; font-weight: 400; text-align: right;
  }
  .contacts li { display: flex; justify-content: flex-end; align-items: center; gap: 12px; height: 24.5px; }
  .contacts svg { width: 20px; height: 20px; flex: none; }

  .tagline {
    position: absolute; left: 121px; top: 273px;
    font-size: 21px; font-weight: 400; letter-spacing: 0.01em;
  }
</style>
</head>
<body>
<main class="canvas">
  <section class="card card--front">
    <div class="clear-panel" role="img" aria-label="Clear card area where the large brand mark decoration sits"></div>
    <div class="wordmark"><span class="wordmark__dot"></span><span>BRONSALK MEDIA</span></div>
    <div class="person">
      <p class="person__name">PAUL ARDLEY</p>
      <p class="person__role">Director Operations</p>
    </div>
    <ul class="contacts">
      <li>+61 452 118 906
        <svg viewBox="0 0 20 20" aria-hidden="true"><rect width="20" height="20" fill="#fff"/><rect x="6.5" y="3" width="7" height="14" rx="1" fill="none" stroke="#19191b" stroke-width="1.4"/><line x1="8.5" y1="14.5" x2="11.5" y2="14.5" stroke="#19191b" stroke-width="1.2"/></svg>
      </li>
      <li>paulardley@bronsalk.com
        <svg viewBox="0 0 20 20" aria-hidden="true"><rect width="20" height="20" fill="#fff"/><rect x="3" y="5" width="14" height="10" fill="none" stroke="#19191b" stroke-width="1.4"/><path d="M3 5l7 6 7-6M3 15l5-5M17 15l-5-5" fill="none" stroke="#19191b" stroke-width="1.2"/></svg>
      </li>
      <li>www.bronsalk.com
        <svg viewBox="0 0 20 20" aria-hidden="true"><rect width="20" height="20" fill="#fff"/><circle cx="10" cy="10" r="6" fill="none" stroke="#19191b" stroke-width="1.3"/><ellipse cx="10" cy="10" rx="2.6" ry="6" fill="none" stroke="#19191b" stroke-width="1.1"/><line x1="4" y1="10" x2="16" y2="10" stroke="#19191b" stroke-width="1.1"/></svg>
      </li>
    </ul>
  </section>

  <section class="card card--back">
    <div class="clear-panel" role="img" aria-label="Clear card area where the large brand mark decoration sits"></div>
    <div class="wordmark"><span>BRONSALK MEDIA</span></div>
    <p class="tagline">Create Inspire Tomorrow</p>
  </section>
</main>
</body>
</html>
```